Wood Fired Pizza business needs a business card design

We need a business car design for a new company based in Texas called "Crusti Fern" a play off of Dusty Fern. We hand craft pizzas and cook them in our wood fired oven at temp. that reach 900 degrease, allowing the pizza to cook in 90 sec. Our customer base is private catering, festivals, and farmers markets. We would like to see designs that follow the Dusty Fern brand of Camoflauge, and Orange text. The final design should communicate pizza cooked in a wood fired oven.

```html
<!DOCTYPE html>
<html lang="en">
<head>
<meta charset="utf-8">
<title>Crusti Fern — Business Card</title>
<link rel="stylesheet" href="https://fonts.googleapis.com/css2?family=Teko:wght@600&family=Ubuntu:wght@400&display=swap">
<style>
  :root {
    --page-bg: #e9e6e1;
    --card-red: #c9070d;
    --card-red-deep: #a30409;
    --ember-orange: #f0a01c;
    --ink: #141010;
    --text-light: #fbe9e6;
    --fire-bright: #f5872a;
    --crust-light: #e3b6a0;
    --char-dark: #3a0f0b;
  }
  * { box-sizing: border-box; margin: 0; padding: 0; }
  html, body {
    width: 1200px;
    height: 900px;
    overflow: hidden;
    background: var(--page-bg);
  }
  .canvas {
    width: 1200px;
    height: 900px;
    display: flex;
    align-items: center;
    justify-content: center;
  }
  .business-card {
    position: relative;
    width: 1050px;
    height: 600px;
    background: linear-gradient(160deg, var(--card-red) 0%, var(--card-red) 55%, var(--card-red-deep) 100%);
    overflow: hidden;
    box-shadow: 0 10px 30px rgba(0, 0, 0, 0.18);
  }
  .oven-photo {
    position: absolute;
    right: 0;
    bottom: 0;
    width: 660px;
    height: 470px;
    background:
      radial-gradient(ellipse 38% 30% at 42% 62%, var(--crust-light) 0%, rgba(227, 182, 160, 0.55) 45%, rgba(227, 182, 160, 0) 100%),
      radial-gradient(ellipse 40% 35% at 78% 28%, var(--fire-bright) 0%, rgba(245, 135, 42, 0.5) 45%, rgba(245, 135, 42, 0) 100%),
      radial-gradient(ellipse 45% 40% at 85% 55%, var(--char-dark) 0%, rgba(58, 15, 11, 0.6) 50%, rgba(58, 15, 11, 0) 100%),
      radial-gradient(ellipse 60% 45% at 50% 100%, rgba(90, 30, 25, 0.85) 0%, rgba(90, 30, 25, 0) 100%);
  }
  .brand-name {
    position: absolute;
    left: 250px;
    top: 40px;
    font-family: "Teko", "Arial Narrow", sans-serif;
    font-weight: 600;
    font-size: 96px;
    line-height: 1;
    letter-spacing: 2px;
    text-transform: uppercase;
    color: var(--ink);
  }
  .contact {
    position: absolute;
    left: 118px;
    top: 180px;
    font-family: "Ubuntu", "Segoe UI", sans-serif;
    font-size: 21px;
    line-height: 1.45;
    color: var(--text-light);
  }
  .contact-address { margin-bottom: 34px; }
  .contact-list { list-style: none; }
  .contact-item {
    position: relative;
    margin-bottom: 8px;
  }
  .contact-icon {
    position: absolute;
    left: -44px;
    top: 4px;
    width: 20px;
    height: 20px;
  }
  .contact-icon * {
    fill: none;
    stroke: var(--ember-orange);
    stroke-width: 1.8;
    stroke-linejoin: round;
    stroke-linecap: round;
  }
</style>
</head>
<body>
  <main class="canvas">
    <article class="business-card">
      <div class="oven-photo" role="img" aria-label="Photo of a pizza baking beside glowing flames and embers in a wood-fired oven"></div>

      <h1 class="brand-name">Crusti Fern</h1>

      <section class="contact">
        <address class="contact-address">
          Emberline, Inc<br>
          2480 Cedar Hollow Rd<br>
          Austin, TX 78745
        </address>
        <ul class="contact-list">
          <li class="contact-item">
            <svg class="contact-icon" viewBox="0 0 20 20" aria-hidden="true">
              <path d="M5 2h4l1 4-2 2a10 10 0 0 0 4 4l2-2 4 1v4a2 2 0 0 1-2 2A15 15 0 0 1 3 4a2 2 0 0 1 2-2z"/>
            </svg>
            (512) 555-0148
          </li>
          <li class="contact-item">
            <svg class="contact-icon" viewBox="0 0 20 20" aria-hidden="true">
              <rect x="5" y="1.5" width="10" height="17" rx="2"/>
              <line x1="9" y1="15.5" x2="11" y2="15.5"/>
            </svg>
            (512) 555-0193
          </li>
          <li class="contact-item">
            <svg class="contact-icon" viewBox="0 0 20 20" aria-hidden="true">
              <rect x="2" y="4" width="16" height="12" rx="1.5"/>
              <polyline points="2.5,4.5 10,11 17.5,4.5"/>
            </svg>
            marla@crustifern.com
          </li>
        </ul>
      </section>
    </article>
  </main>
</body>
</html>
```